Real Estate Website

I have a very old website that was built almost 20 years ago. We are rebuilding it and need a fresh new design for it please.
The existing website is https://northpeakhomes.example

This is for a real estate company that is selling real estate in Hokkaido, Japan (known for it's skiing and snow tourism) and is all in english as it targets westerners looking to buy holiday homes or investment properties.
Updates

Hi everyone.

Sorry this has taken so long to get back to you. My client has taken a long time to get back to me after the Christmas break.

Unfortunately they did not want to go ahead with any of the designs submitted as they said they look too much like business sales websites instead of residential and commercial sales. An example of what they lik is https://www.velmorproperty.example/
They don't want it to look at all like their business sales website (https://www.ranscombebusinesssales.example/) and have said:

• keep Ra NSCOMBE GROUP logo and color scheme the same
• Give freedom to the designers, on how what to execute what the company does.
-Commercial/Industrial
-Residential

Make them separate as there’s a different audience of clients for commercial & residential are very different.

I will provide some content and headings which you have the freedom to play around and coordinate. What I provide below are only suggestions, please feel free to be use your ideas and be innovative.

Residential listings - would like the listing to shows Features on details page.
Commercial listings – must display “building area” on the front page
HEADINGS ON TOP OF PAGE -TABS:
HOME - This MUST show on the tab
COMMERCIAL/INDUSTRIAL - This MUST show on the tab
RESIDENTIAL - This MUST show on the tab
BUSINESS SALES (this to link straight to my RANSCOMBE BUSINESS SALES & VUALUATIONS website - This MUST show on the tab
ABOUT US
BLOGS/videos- I want my team to be able to load all the videos, eg when they do videos for auctions, developments etc -– optional, if not enough space, show it on the bottom of the website ( you could also add under ABOUT US tab)
CONTACT US

Maybe show this on the home screen heading:
Specialists in Commercial/ Industrial Property,
Trusted in Residential Property

Theme:
“Maximising returns, protecting investments, expert property advisory”
Work With Us

The Information below is not in any particle order:

Book an Appraisal
Discover the Real Value of Your Property
At Ranscombe Group, we don’t just provide standard appraisals — we deliver strategic, insight-driven reports that uncover the true drivers of your property’s worth. Whether it’s commercial, industrial, or residential, our expertise ensures you see the full picture.
From market trends and rental potential to investment performance and future growth opportunities, our tailored reports give you clarity, confidence, and actionable insights.
Book a confidential consultation today and gain the expert guidance you need to maximise returns and make smarter property decisions.

What We Do
What We Do – Property Management, Sales & Leasing
At Ranscombe Group, we specialise in guiding property owners, investors, and landlords through the complexities of managing, selling, leasing, and valuing assets. Our mission is clear: to deliver clarity, confidence, and measurable results at every stage of your property journey.
We go beyond standardised reports. Our strategic, insight-driven valuations and management solutions uncover the true drivers of your property’s performance. From tailored marketing campaigns and compelling listings to confidential negotiations and introductions, we ensure your asset attracts the right tenants, buyers, or investors.
When the future of your investment is on the line, you need more than a property manager or agent — you need a partner who delivers certainty, strategy, and results. At Ranscombe Group, we don’t just manage, lease, or sell properties; we maximise value, income, and long-term growth.
Contact us today for a confidential consultation and discover how Ranscombe Group can help you achieve the strongest outcomes for your property portfolio.

Who We Are
At Ranscombe Group, we are recognised as a trusted authority in commercial and residential property management, sales, and leasing. Property owners, investors, and developers turn to us for our proven expertise, discretion, and consistent results.
Our mission is to set the standard for excellence in property services. Guided by innovation, integrity, and strategic execution, we deliver outcomes that protect assets, maximise returns, and create enduring value for our clients.
Whether your goal is to manage your investment, increase rental income, lease to the right tenants, or achieve a successful sale, we provide clarity, confidence, and tailored solutions at every stage of the journey.
Let’s begin the conversation today — and explore how Ranscombe Group can help you achieve the strongest results for your property portfolio.

Commercial & Industrial Property Management & Leasing

At Ranscombe Group, we are recognised as a leading authority in the management and leasing of premium commercial and industrial assets. Trusted by investors, landlords, and developers, our portfolio spans medical centres, healthcare facilities, allied health clinics, global franchise brands such as BWQ and The Marmalade Pantry, high‑end retail outlets, and large‑scale industrial and manufacturing properties.
We deliver strategic, results‑driven property solutions that combine market intelligence, operational excellence, and meticulous attention to detail. Our approach is designed to maximise returns, minimise vacancies, and safeguard long‑term asset performance.

Our Services
• Strategic Marketing & Leasing – Positioning your property to attract premium tenants through targeted, multi‑channel campaigns.
• Tenant & Lease Administration – Precision management of agreements, renewals, compliance, and documentation.
• Revenue Optimisation – Proactive rent collection, vacancy minimisation, and lease structuring to elevate asset value.
• Maintenance & Property Upkeep – Access to vetted, high‑quality trades for repairs and preventative care, ensuring assets remain in peak condition.
• Regulatory Compliance & Essential Services – Full oversight of statutory obligations and essential service measures, protecting both compliance and reputation.
Why Choose us
• Sector Expertise – Deep knowledge across medical, healthcare, franchise, retail, and industrial sectors, enabling tailored strategies for each asset class.
• Proactive Asset Management – Beyond operations, we actively enhance value, mitigate risk, and secure the right tenants.
• Bespoke Solutions – Every property is unique. We craft customised management and leasing strategies aligned with your objectives and market conditions.
• Professional Excellence – Integrity, precision, and industry‑leading best practices deliver measurable results and peace of mind for discerning property owners.
With Ranscombe Group, your commercial and industrial assets are managed with authority, insight, and excellence — ensuring performance that meets the expectations of high‑end investors and developers.

```html
<!DOCTYPE html>
<html lang="en">
<head>
<meta charset="utf-8">
<title>Northpeak Homes – Hokkaido Property</title>
<link href="https://fonts.googleapis.com/css2?family=Barlow:wght@400;500;600;700&family=DM+Serif+Display&display=swap" rel="stylesheet">
<style>
:root{
  --red:#cf2b27;
  --red-dark:#b52320;
  --ink:#222222;
  --text:#3b3b3b;
  --muted:#8a8a8a;
  --line:#dcdcdc;
  --dark:#262626;
  --white:#ffffff;
  --serif:'DM Serif Display', serif;
  --sans:'Barlow', sans-serif;
}
*{box-sizing:border-box;margin:0;padding:0}
html,body{width:1200px;height:3715px;overflow:hidden}
body{position:relative;background:var(--white);font-family:var(--sans);color:var(--text)}
.abs{position:absolute}
a{color:inherit;text-decoration:none}

/* top bar */
.topbar{left:141px;top:0;width:918px;height:39px;border-bottom:1px solid #ececec}
.topbar .social{position:absolute;left:0;top:13px;display:flex;gap:8px}
.topbar .social span{width:11px;height:11px;background:var(--red);display:block}
.topbar .contact{position:absolute;right:0;top:11px;display:flex;gap:12px;font-size:12px;color:var(--ink);align-items:center}
.topbar .contact svg{vertical-align:middle;margin-right:5px}

/* header */
.brand{display:flex;align-items:center;gap:8px;color:var(--red)}
.brand .mark{width:16px;height:16px;border-radius:50%;background:var(--red)}
.brand .name{font-family:var(--serif);line-height:1;letter-spacing:.5px}
.brand .name b{display:block;font-weight:400}
.header-brand{left:141px;top:58px}
.header-brand .name b:first-child{font-size:22px}
.header-brand .name b:last-child{font-size:11px;letter-spacing:1.5px;margin-top:2px}
.nav{right:141px;top:74px;display:flex;gap:19px;font-size:12px;font-weight:500;color:var(--ink);white-space:nowrap}
.nav .active{color:var(--red)}

/* hero */
.hero{left:0;top:125px;width:1200px;height:582px;background:linear-gradient(115deg,#0d1930 0%,#1c2f52 35%,#0e1a2e 60%,#3a3a32 85%,#16203a 100%)}
.hero-tag{left:141px;top:274px;height:30px;padding:0 16px;background:var(--red);color:#fff;font-size:12.5px;line-height:30px}
.hero-title{left:141px;top:314px;font-family:var(--serif);font-size:50px;line-height:56px;color:#fff;letter-spacing:1px;font-weight:400}
.hero-sub{left:141px;top:428px;width:500px;font-size:15px;line-height:23px;color:#fff}
.btn{display:inline-block;text-align:center;font-size:12.5px;font-weight:500;text-transform:uppercase}
.btn-red{background:var(--red);color:#fff}
.hero-view{left:141px;top:499px;width:144px;height:36px;line-height:36px}
.hero-contact{left:297px;top:499px;width:115px;height:36px;line-height:34px;border:1px solid #fff;color:#fff}

/* stats */
.stat{top:707px;height:141px;width:212px;padding:14px 0 0 45px;color:#fff}
.stat .num{font-family:var(--serif);font-size:48px;line-height:1}
.stat .lbl{font-family:var(--serif);font-size:18px;line-height:27px;margin-top:6px;letter-spacing:.5px}
.stat-red{left:252px;background:var(--red)}
.stat-dark{left:464px;background:#2b2b2b}

.svc-card{left:678px;top:635px;width:264px;height:263px;background:#fff;border-top:4px solid var(--red);box-shadow:0 2px 14px rgba(0,0,0,.15);padding:28px 16px 0 14px}
.svc-item{display:flex;gap:13px;margin-bottom:19px}
.svc-item h4{font-size:15px;font-weight:600;color:var(--ink);line-height:18px}
.svc-item p{font-size:12px;line-height:19px;color:#555}

/* labels/titles */
.eyebrow{font-size:15px;color:var(--red);text-transform:uppercase;letter-spacing:.3px}
.title{font-family:var(--serif);font-size:32px;color:var(--ink);letter-spacing:1px;text-transform:uppercase;line-height:1.1;font-weight:400}
.center{left:0;width:1200px;text-align:center}

/* welcome */
.welcome-text{left:141px;top:1090px;width:410px;font-size:13px;line-height:23px;color:var(--ink)}
.read-more{left:141px;top:1321px;width:104px;height:37px;line-height:37px}
.photo-frame{background:#fff;box-shadow:0 3px 14px rgba(0,0,0,.15);padding:10px}
.photo-frame .ph{width:100%;height:100%}
.snow-fade{left:820px;top:1150px;width:380px;height:280px;background:radial-gradient(ellipse at 40% 50%,#e6e6e6 0%,rgba(255,255,255,0) 70%)}
.play{left:756px;top:1060px;width:75px;height:75px;background:var(--red)}

/* listings */
.tab{top:1566px;height:29px;line-height:27px;font-size:12px;text-align:center;border:1px solid #cfcfcf;color:#9a9a9a;text-transform:uppercase}
.tab.on{background:var(--red);border-color:var(--red);color:#fff}
.card{top:1619px;width:212px;height:371px;background:#fff;border:1px solid #eee}
.card.hl{background:#ebebeb}
.card .ph{height:178px;position:relative}
.card .kind{position:absolute;left:10px;top:10px;height:20px;line-height:20px;padding:0 8px;background:var(--red);color:#fff;font-size:10.5px;font-weight:600;letter-spacing:.4px;text-transform:uppercase}
.card .kind.com{background:var(--dark)}
.card h5{margin:18px 0 0 15px;font-size:12.5px;font-weight:600;color:var(--ink);text-transform:uppercase}
.card .loc{margin:4px 0 0 15px;font-size:12px;color:#aaa;display:flex;align-items:center;gap:5px}
.card p{margin:9px 15px 0;font-size:11px;line-height:16px;color:#444;height:48px;overflow:hidden}
.card .price{margin:8px 15px 0;font-size:15px;color:var(--red);font-weight:500;display:flex;justify-content:space-between;align-items:baseline}
.card .price small{font-size:11px;color:#555;font-weight:500}
.card .go{position:absolute;left:0;bottom:0;width:100%;height:35px;line-height:35px;background:var(--dark);color:#fff;text-align:center;font-size:12.5px;font-weight:500}
.card.hl .go{background:var(--red)}
.arrow{top:1781px;width:30px;height:30px;display:flex;align-items:center;justify-content:center}
.view-all{left:548px;top:2027px;width:104px;height:38px;line-height:38px}

/* process */
.process-fade{left:0;top:2430px;width:600px;height:290px;background:radial-gradient(ellipse at 45% 40%,#e2e2e2 0%,rgba(255,255,255,0) 68%)}
.process-intro{left:647px;top:2252px;width:420px;font-size:13px;line-height:19.5px;color:var(--ink)}
.step{left:647px;width:420px}
.step h6{font-size:16px;font-weight:500;color:var(--red);letter-spacing:.6px;text-transform:uppercase;line-height:20px}
.step p{font-size:12.6px;line-height:19px;color:var(--ink);margin-top:2px}

/* testimonial */
.quote-text{left:221px;top:2944px;width:440px;font-size:15px;line-height:23.5px;color:var(--ink);font-weight:500}
.stars{left:221px;top:2911px;display:flex;gap:3px}
.who{left:221px;top:3073px}
.who b{display:block;color:var(--red);font-weight:500;font-size:15px}
.who span{font-size:12px;color:#444}
.dots{left:223px;top:3124px;display:flex;gap:5px;align-items:center}
.dots i{width:9px;height:9px;border-radius:50%;background:#ccc;display:block}
.dots i.on{width:14px;height:14px;background:var(--red)}

/* footer */
.foot-red{left:0;top:3304px;width:395px;height:411px;background:var(--red)}
.foot-dark{left:395px;top:3304px;width:805px;height:411px;background:var(--dark)}
.foot-brand{left:141px;top:3366px;color:#fff}
.foot-brand .mark{background:#fff}
.foot-brand .name{color:#fff}
.foot-brand .name b:first-child{font-size:24px}
.foot-brand .name b:last-child{font-size:12px;letter-spacing:1.5px;margin-top:2px}
.fc{left:141px;color:#fff;display:flex;gap:14px}
.fc small{display:block;font-size:11.5px;text-transform:uppercase}
.fc strong{display:block;font-weight:500}
.foot-line-red{left:0;top:3648px;width:395px;height:1px;background:rgba(255,255,255,.35)}
.foot-line-dark{left:395px;top:3648px;width:665px;height:1px;background:#5a5a5a}
.sq{top:3667px;width:32px;height:32px;background:var(--dark);display:flex;align-items:center;justify-content:center}
.sq span{width:10px;height:10px;background:#fff;display:block}
.foot-h{font-size:15px;color:#fff;text-transform:uppercase;font-weight:500}
.links{top:3451px;font-size:12.5px;line-height:20.5px;color:#ddd}
.links li{list-style:none;white-space:nowrap}
.links li::before{content:"» ";color:#fff}
.badge{left:474px;top:3575px;width:180px;height:46px;border:1px solid #bbb;border-radius:2px}
.guide{left:770px;top:3451px;width:300px;font-size:12px;line-height:19px;color:#ddd}
.email-in{left:770px;top:3513px;width:288px;height:37px;background:#fff;color:#333;font-size:12.5px;line-height:37px;padding-left:12px}
.download{left:770px;top:3563px;width:176px;height:38px;line-height:38px;font-size:16px}
.copy{left:395px;width:665px;top:3675px;text-align:center;font-size:12px;color:#ccc}
</style>
</head>
<body>

<!-- top bar -->
<div class="abs topbar">
  <div class="social"><span></span><span></span><span></span><span></span></div>
  <div class="contact">
    <span><svg width="14" height="14" viewBox="0 0 24 24" fill="none" stroke="#cf2b27" stroke-width="2"><path d="M5 3h4l2 5-3 2a12 12 0 0 0 6 6l2-3 5 2v4a2 2 0 0 1-2 2A17 17 0 0 1 3 5a2 2 0 0 1 2-2z"/></svg>+81 136 40 5280</span>
    <span><svg width="16" height="12" viewBox="0 0 24 18"><rect width="24" height="18" rx="2" fill="#cf2b27"/><path d="M2 3l10 7 10-7" fill="none" stroke="#fff" stroke-width="2"/></svg>info@northpeakhomes.example</span>
  </div>
</div>

<!-- header -->
<a class="abs brand header-brand" href="https://northpeakhomes.example"><span class="mark"></span><span class="name"><b>NORTHPEAK</b><b>HOMES.EXAMPLE</b></span></a>
<nav class="abs nav">
  <a class="active">HOME</a><a>COMMERCIAL/INDUSTRIAL</a><a>RESIDENTIAL</a><a>BUSINESS SALES</a><a>ABOUT US</a><a>BLOGS/VIDEOS</a><a>CONTACT US</a>
</nav>

<!-- hero -->
<div class="abs hero" role="img" aria-label="Photo looking up at glass office towers at dusk with the sun flaring between buildings"></div>
<div class="abs hero-tag">We construct and manage spaces and infrastructure</div>
<h1 class="abs hero-title">Discover Your Dream<br>Hokkaido Property</h1>
<p class="abs hero-sub">Exclusive ski chalets, luxury apartments, and investment properties in Japan's most sought-after winter destinations</p>
<a class="abs btn btn-red hero-view">View Properties</a>
<a class="abs btn hero-contact">Contact Us</a>

<div class="abs stat stat-red"><div class="num">400+</div><div class="lbl">Completed<br>Projects</div></div>
<div class="abs stat stat-dark"><div class="num">20+</div><div class="lbl">Years<br>Experience</div></div>

<div class="abs svc-card">
  <div class="svc-item">
    <svg width="40" height="46" viewBox="0 0 40 46" fill="none" stroke="#cf2b27" stroke-width="1.6"><path d="M6 2h20l8 8v32H6z"/><path d="M26 2v8h8M11 16h16M11 22h16M11 28h10"/></svg>
    <div><h4>General Contract</h4><p>Lorem ipsum dolor sit amet, consectetuer adipiscing elit, sed</p></div>
  </div>
  <div class="svc-item">
    <svg width="40" height="46" viewBox="0 0 40 46" fill="none" stroke="#cf2b27" stroke-width="1.6"><rect x="10" y="2" width="26" height="34"/><path d="M15 10h16M15 16h16M15 22h10"/><path d="M2 44V32l8-7 8 7v12z"/></svg>
    <div><h4>Project Planning</h4><p>Lorem ipsum dolor sit amet, consectetuer adipiscing elit, sed</p></div>
  </div>
  <div class="svc-item">
    <svg width="40" height="46" viewBox="0 0 40 46" fill="none" stroke="#cf2b27" stroke-width="1.6"><path d="M3 22L20 6l17 16M8 18v24h24V18"/><path d="M16 42V30h8v12"/></svg>
    <div><h4>Refurbishment</h4><p>Lorem ipsum dolor sit amet, consectetuer adipiscing elit, sed</p></div>
  </div>
</div>

<!-- welcome -->
<div class="abs eyebrow" style="left:141px;top:1013px">Welcome to</div>
<h2 class="abs title" style="left:141px;top:1038px">Northpeak Homes</h2>
<div class="abs welcome-text">
  <p>An investment in Hokkaido property offers tremendous potential for both lifestyle and financial returns. But, the market is complex and dynamic. To invest wisely you need advice on all the potential pitfalls.</p>
  <p>The Northpeak Homes team is small and dedicated group of professionals focused on delivering the best outcome for our clients whilst never compromising our ethical standards. As a result, we have some very loyal and long-time clients whom we have assisted to buy and sell properties for more than 15 years.</p>
</div>
<a class="abs btn btn-red read-more">Read More</a>

<div class="abs snow-fade"></div>
<div class="abs photo-frame" style="left:815px;top:983px;width:243px;height:243px"><div class="ph" role="img" aria-label="Photo of snow-covered timber chalets lit warmly at dusk below a mountain" style="background:linear-gradient(180deg,#3f5f8f 0%,#6c4a3a 55%,#8a3e2a 75%,#d9d9d9 100%)"></div></div>
<div class="abs photo-frame" style="left:646px;top:1110px;width:245px;height:286px"><div class="ph" role="img" aria-label="Photo of three colleagues meeting around a table with a laptop in a bright office" style="background:linear-gradient(160deg,#eef1ef 0%,#c9cfcc 45%,#8b8f93 70%,#b58c66 100%)"></div></div>
<div class="abs play"><svg width="75" height="75" viewBox="0 0 75 75"><circle cx="37.5" cy="37.5" r="14" fill="#fff"/><path d="M33 30l11 7.5L33 45z" fill="#cf2b27"/></svg></div>

<!-- listings -->
<div class="abs eyebrow center" style="top:1485px">What we do</div>
<h2 class="abs title center" style="top:1509px">Our Services</h2>
<div class="abs tab" style="left:329px;width:164px">Residential</div>
<div class="abs tab on" style="left:500px;width:185px">Commercial / Industrial</div>
<div class="abs tab" style="left:694px;width:176px">Recent Property Sales</div>

<div class="abs arrow" style="left:100px;background:#d5d5d5"><svg width="14" height="12" viewBox="0 0 14 12"><path d="M13 6H2M6 1L1 6l5 5" fill="none" stroke="#fff" stroke-width="2"/></svg></div>
<div class="abs arrow" style="left:1069px;background:#eea5a3"><svg width="14" height="12" viewBox="0 0 14 12"><path d="M1 6h11M8 1l5 5-5 5" fill="none" stroke="#fff" stroke-width="2"/></svg></div>

<div class="abs card" style="left:141px">
  <div class="ph" role="img" aria-label="Photo of an apartment interior with a staircase and wooden floor" style="background:linear-gradient(160deg,#f1eeea 0%,#cfc8be 50%,#5e4a3a 100%)"><span class="kind">Residential</span></div>
  <h5>Sapporo Central Apartments</h5>
  <div class="loc"><svg width="10" height="12" viewBox="0 0 10 12"><circle cx="5" cy="4" r="3" fill="none" stroke="#aaa"/><path d="M1 12c0-3 8-3 8 0" fill="none" stroke="#aaa"/></svg>Sapporo, Hokkaido</div>
  <p>Lorem ipsum dolor sit amet, consect etuer adipiscing elit, sed diam non ummy nibh euismod tincidunt</p>
  <div class="price">¥320,000,000</div>
  <a class="go">VIEW DETAILS ➜</a>
</div>
<div class="abs card hl" style="left:376px">
  <div class="ph" role="img" aria-label="Photo of a modern luxury villa with stone facade and lit windows" style="background:linear-gradient(170deg,#7e96b5 0%,#4a4f55 50%,#7a6148 75%,#5c6b4a 100%)"><span class="kind">Residential</span></div>
  <h5>Furano Luxury Villa</h5>
  <div class="loc"><svg width="10" height="12" viewBox="0 0 10 12"><circle cx="5" cy="4" r="3" fill="none" stroke="#aaa"/><path d="M1 12c0-3 8-3 8 0" fill="none" stroke="#aaa"/></svg>Furano, Hokkaido</div>
  <p>Lorem ipsum dolor sit amet, consect etuer adipiscing elit, sed diam non ummy nibh euismod tincidunt</p>
  <div class="price">¥845,000,000</div>
  <a class="go">VIEW DETAILS ➜</a>
</div>
<div class="abs card" style="left:611px">
  <div class="ph" role="img" aria-label="Photo of an empty open-plan office floor with large windows" style="background:linear-gradient(175deg,#d9dcdf 0%,#b8bcc0 45%,#7d8288 100%)"><span class="kind com">Commercial</span></div>
  <h5>Kiroro Business Office</h5>
  <div class="loc"><svg width="10" height="12" viewBox="0 0 10 12"><circle cx="5" cy="4" r="3" fill="none" stroke="#aaa"/><path d="M1 12c0-3 8-3 8 0" fill="none" stroke="#aaa"/></svg>Kiroro, Hokkaido</div>
  <p>Lorem ipsum dolor sit amet, consect etuer adipiscing elit, sed diam non ummy nibh euismod tincidunt</p>
  <div class="price">¥45,000,000<small>Building area 420 m²</small></div>
  <a class="go">VIEW DETAILS ➜</a>
</div>
<div class="abs card" style="left:846px">
  <div class="ph" role="img" aria-label="Photo of a glowing timber mountain retreat among snowy pine trees" style="background:linear-gradient(180deg,#2e3f5c 0%,#5a4030 50%,#c07a3a 70%,#e8ecef 100%)"><span class="kind com">Commercial</span></div>
  <h5>Modern Mountain Retreat</h5>
  <div class="loc"><svg width="10" height="12" viewBox="0 0 10 12"><circle cx="5" cy="4" r="3" fill="none" stroke="#aaa"/><path d="M1 12c0-3 8-3 8 0" fill="none" stroke="#aaa"/></svg>Niseko, Hokkaido</div>
  <p>Lorem ipsum dolor sit amet, consect etuer adipiscing elit, sed diam non ummy nibh euismod tincidunt</p>
  <div class="price">¥245,000,000<small>Building area 610 m²</small></div>
  <a class="go">VIEW DETAILS ➜</a>
</div>
<a class="abs btn btn-red view-all">View All</a>

<!-- process -->
<div class="abs process-fade"></div>
<div class="abs photo-frame" style="left:141px;top:2183px;width:318px;height:309px"><div class="ph" role="img" aria-label="Photo of a small team gathered around a computer in an office" style="background:linear-gradient(150deg,#e9edf1 0%,#c4cad1 40%,#3a3d44 75%,#8d939a 100%)"></div></div>
<div class="abs photo-frame" style="left:310px;top:2372px;width:241px;height:202px"><div class="ph" role="img" aria-label="Photo of hands working with a laptop, documents and a small building model" style="background:linear-gradient(160deg,#8aa4c0 0%,#d8dde2 50%,#b89a7c 100%)"></div></div>

<div class="abs eyebrow" style="left:647px;top:2179px">Our client</div>
<h2 class="abs title" style="left:647px;top:2203px">Focused Process</h2>
<p class="abs process-intro">We've perfected our approach over 20 years to ensure a smooth, transparent property acquisition experience for Western buyers.</p>
<div class="abs step" style="top:2300px"><h6>Initial Consultation</h6><p>We listen to your needs, budget, and preferences to understand exactly what you're looking for in a Hokkaido property.</p></div>
<div class="abs step" style="top:2373px"><h6>Viewing &amp; Evaluation</h6><p>We arrange viewings and provide expert analysis on each property's value, potential, and any considerations.</p></div>
<div class="abs step" style="top:2445px"><h6>Negotiation &amp; Purchase</h6><p>We handle all negotiations, legal processes, and paperwork to ensure a smooth purchase at the best possible terms.</p></div>
<div class="abs step" style="top:2518px"><h6>After-Sale Support</h6><p>Our service continues after purchase with property management recommendations and local connections.</p></div>

<!-- testimonials -->
<div class="abs eyebrow center" style="top:2709px">Client stories</div>
<h2 class="abs title center" style="top:2733px">What Our Clients Say</h2>
<svg class="abs" style="left:221px;top:2870px" width="40" height="30" viewBox="0 0 40 30"><path d="M0 30V14C0 5 4 1 12 0v6c-4 1-5 3-5 7h5v17zM22 30V14c0-9 4-13 12-14v6c-4 1-5 3-5 7h5v17z" fill="#cf2b27"/></svg>
<div class="abs stars">
  <svg width="86" height="14" viewBox="0 0 86 14" fill="#e8492a"><g id="st"><path d="M7 0l2 5h5l-4 3 1.5 5L7 10l-4.5 3L4 8 0 5h5z"/></g><use href="#st" x="18"/><use href="#st" x="36"/><use href="#st" x="54"/><use href="#st" x="72"/></svg>
</div>
<p class="abs quote-text">Lorem ipsum dolor sit amet, consectetuer adipiscing elit, sed diam nonummy nibh euismod tincidunt ut laoreet dolore magna aliquam erat volutpat. Ut wisi enim ad minim veniam, quis nostrud exerci tation ullamcorper suscipit lobortis nisl ut aliquip ex ea commodo consequat.</p>
<div class="abs who"><b>MARA HOLT</b><span>Hong Kong</span></div>
<div class="abs dots"><i class="on"></i><i></i><i></i></div>
<svg class="abs" style="left:310px;top:3090px" width="380" height="60" viewBox="0 0 380 60" fill="none" stroke="#d0d0d0" stroke-width="1"><path d="M0 40c20-10 30 0 50 5 15-20 40-20 60 5 30-5 60 10 90 0 20-8 40-5 60 0 40 5 80-30 120-38"/><path d="M0 58h380"/></svg>
<div class="abs photo-frame" style="left:689px;top:2812px;width:280px;height:381px"><div class="ph" role="img" aria-label="Photo of a dark modern hallway with a wooden staircase and light floor" style="background:linear-gradient(165deg,#2f3338 0%,#4a4e54 45%,#b8b3aa 80%,#d9d4cb 100%)"></div></div>

<!-- footer -->
<div class="abs foot-red"></div>
<div class="abs foot-dark"></div>
<a class="abs brand foot-brand" href="https://northpeakhomes.example"><span class="mark"></span><span class="name"><b>NORTHPEAK</b><b>HOMES.EXAMPLE</b></span></a>

<div class="abs fc" style="top:3461px">
  <svg width="28" height="28" viewBox="0 0 24 24" fill="none" stroke="#fff" stroke-width="1.4"><path d="M5 3h4l2 5-3 2a12 12 0 0 0 6 6l2-3 5 2v4a2 2 0 0 1-2 2A17 17 0 0 1 3 5a2 2 0 0 1 2-2z"/></svg>
  <div><small>Phone</small><strong style="font-size:19px">+81 136 40 5280</strong></div>
</div>
<div class="abs fc" style="top:3516px">
  <svg width="28" height="28" viewBox="0 0 24 24" fill="none" stroke="#fff" stroke-width="1.4"><rect x="2" y="5" width="20" height="15"/><path d="M2 6l10 7 10-7"/></svg>
  <div><small>Email</small><strong style="font-size:12.5px">info@northpeakhomes.example</strong></div>
</div>
<div class="abs fc" style="top:3562px">
  <svg width="28" height="28" viewBox="0 0 24 24" fill="none" stroke="#fff" stroke-width="1.4"><circle cx="12" cy="12" r="10"/><path d="M2 12h20M12 2c3 3 3 17 0 20M12 2c-3 3-3 17 0 20"/></svg>
  <div><small>Address</small><strong style="font-size:12.5px;line-height:18px">123, Building Name, Street<br>City, State XY 123456</strong></div>
</div>
<div class="abs foot-line-red"></div>
<div class="abs foot-line-dark"></div>
<div class="abs sq" style="left:141px"><span></span></div>
<div class="abs sq" style="left:180px"><span></span></div>
<div class="abs sq" style="left:219px"><span></span></div>
<div class="abs sq" style="left:258px"><span></span></div>

<div class="abs foot-h" style="left:474px;top:3410px">Quick Links</div>
<ul class="abs links" style="left:474px"><li>Home</li><li>Commercial</li><li>Residential</li><li>Business Sales</li><li>About Us</li></ul>
<ul class="abs links" style="left:607px"><li>Blogs/Videos</li><li>Career</li><li>Our Team</li><li>Contact Us</li></ul>
<div class="abs badge"></div>

<div class="abs foot-h" style="left:770px;top:3410px">Free Investment Guide</div>
<p class="abs guide">Download our comprehensive guide to buying property in Japan. Learn about the process, legal requirements, financing options, and market trends.</p>
<div class="abs email-in">Your email address</div>
<a class="abs btn btn-red download">DOWNLOAD NOW</a>

<div class="abs copy">© 2026 Northpeak Homes. All Rights Reserved.</div>

</body>
</html>
```